Business Card for supplement company

Company Name: Brimcrest Nutrition
We require quite a simple yet stand out business card for our supplement company.
We are selling high end bodybuilding supplements direct to the public through online sales and Facebook marketing.
There will be slightly varying versions of the card and the winning design will be required to make these slight adjustments.
We will also require the file to be provided in and editable version as we will have a discount code on there that will be changed for different people.
Employee Cards:
Logo on the front of the card (see attached EPS file)
Please also add slogan in text "Built for the Final Repetition" as close as possible to what is seen in this link www.brimcrestnutrition.example.com.au
Suggestions: Card in black, possibly use a similar background to website theme (honeycomb, carbon look)
Information to be included on the back (please place and order accordingly)
:Tarq Welmsby (Director)
Email: tarq@brimcrestnutrition.example.com.au
Phone: 02 5918 2273
Website: www.brimcrestnutrition.example.com.au
Athlete Cards:
Front:
Same as above
Back:
Discount Code: xxx123 (to be editable)
Facebook: www.socialsite.example/BrimcrestNutrition
Design ideas: please look at our website and facebook signup page for design ideas.

```html
<!DOCTYPE html>
<html lang="en">
<head>
<meta charset="utf-8">
<title>Brimcrest Nutrition – Business Cards</title>
<link rel="stylesheet" href="https://fonts.googleapis.com/css2?family=Cinzel:wght@400;700&family=Open+Sans:wght@400;700&display=swap">
<style>
  :root {
    --stage: #0d3a12;
    --card-dark: #0c0c0c;
    --card-mid: #262626;
    --brand-green: #35d62a;
    --slogan-gold: #e8c62a;
    --photo-skin: #b07a5c;
    --photo-mid: #6b4532;
    --photo-shadow: #1a1410;
    --icon-cut: #0c0c0c;
  }
  * { box-sizing: border-box; margin: 0; padding: 0; }
  html, body {
    width: 1200px; height: 1000px; overflow: hidden;
    background: var(--stage);
  }
  .canvas { position: relative; width: 1200px; height: 1000px; }
  .card {
    position: absolute; left: 250px; width: 700px; height: 400px;
    border-radius: 6px; overflow: hidden;
    background: radial-gradient(ellipse at 40% 40%, var(--card-mid) 0%, var(--card-dark) 75%);
    box-shadow: 0 14px 30px rgba(0,0,0,0.55);
  }
  .card--front { top: 70px; }
  .card--back  { top: 530px; }

  .wordmark {
    font-family: "Open Sans", sans-serif; font-weight: 700;
    color: var(--brand-green); letter-spacing: 1px; line-height: 1;
    display: flex; align-items: center; gap: 14px; white-space: nowrap;
  }
  .wordmark__dot { display: inline-block; border-radius: 50%; background: var(--brand-green); }
  .slogan {
    font-family: "Cinzel", serif; font-weight: 700;
    color: var(--slogan-gold); font-variant: small-caps; letter-spacing: 1px;
    white-space: nowrap;
  }

  /* Front */
  .front__brand {
    position: absolute; left: 0; right: 0; top: 105px;
    display: flex; flex-direction: column; align-items: center; gap: 22px;
  }
  .front__brand .wordmark { font-size: 54px; }
  .front__brand .wordmark__dot { width: 30px; height: 30px; }
  .front__brand .slogan { font-size: 24px; }
  .front__url {
    position: absolute; left: 0; right: 0; bottom: 70px; text-align: center;
    font-family: "Open Sans", sans-serif; font-size: 19px; color: var(--brand-green);
  }

  /* Back */
  .back__info { position: absolute; left: 40px; top: 48px; width: 360px; }
  .back__info .wordmark { font-size: 28px; gap: 10px; }
  .back__info .wordmark__dot { width: 17px; height: 17px; }
  .back__info .slogan { font-size: 13px; margin-top: 10px; }
  .person__name {
    margin-top: 34px;
    font-family: "Open Sans", sans-serif; font-weight: 700; font-size: 30px;
    color: var(--brand-green); line-height: 1.2;
  }
  .person__role {
    font-family: "Open Sans", sans-serif; font-size: 20px; color: var(--slogan-gold);
    margin-top: 2px;
  }
  .contact-list { list-style: none; margin-top: 24px; }
  .contact-list li {
    display: flex; align-items: center; gap: 8px; margin-bottom: 8px;
    font-family: "Open Sans", sans-serif; font-size: 15px; color: var(--brand-green);
    white-space: nowrap;
  }
  .contact-list svg { width: 17px; height: 17px; flex: none; }
  .athlete-photo {
    position: absolute; right: 0; top: 0; width: 290px; height: 400px;
    background: radial-gradient(ellipse at 50% 40%, var(--photo-skin) 0%, var(--photo-mid) 45%, var(--photo-shadow) 100%);
  }
</style>
</head>
<body>
<main class="canvas">

  <section class="card card--front" aria-label="Card front">
    <div class="front__brand">
      <div class="wordmark"><span class="wordmark__dot"></span>Brimcrest Nutrition</div>
      <p class="slogan">"Built for the Final Repetition"</p>
    </div>
    <p class="front__url">www.brimcrestnutrition.example.com.au</p>
  </section>

  <section class="card card--back" aria-label="Card back">
    <div class="back__info">
      <div class="wordmark"><span class="wordmark__dot"></span>Brimcrest Nutrition</div>
      <p class="slogan">"Built for the Final Repetition"</p>
      <h2 class="person__name">Tarq Welmsby</h2>
      <p class="person__role">Director</p>
      <ul class="contact-list">
        <li>
          <svg viewBox="0 0 20 20" aria-hidden="true"><rect x="1" y="4" width="18" height="12" fill="var(--brand-green)"/><path d="M1 4 L10 11 L19 4" fill="none" stroke="var(--icon-cut)" stroke-width="1.6"/></svg>
          : tarq@brimcrestnutrition.example.com.au
        </li>
        <li>
          <svg viewBox="0 0 20 20" aria-hidden="true"><path d="M2 7 Q10 1 18 7 L16 9 L13 8 L13 6 Q10 5 7 6 L7 8 L4 9 Z" fill="var(--brand-green)"/><rect x="4" y="10" width="12" height="8" rx="1" fill="var(--brand-green)"/></svg>
          : 02 5918 2273
        </li>
        <li>
          <svg viewBox="0 0 20 20" aria-hidden="true"><circle cx="10" cy="10" r="8.5" fill="none" stroke="var(--brand-green)" stroke-width="1.8"/><ellipse cx="10" cy="10" rx="3.5" ry="8.5" fill="none" stroke="var(--brand-green)" stroke-width="1.5"/><line x1="1.5" y1="10" x2="18.5" y2="10" stroke="var(--brand-green)" stroke-width="1.5"/></svg>
          : www.brimcrestnutrition.example.com.au
        </li>
      </ul>
    </div>
    <div class="athlete-photo" role="img" aria-label="Photo of a shirtless boxer in gloves, guard raised"></div>
  </section>

</main>
</body>
</html>
```